Reed & Vale NC grand opening (for BILLBOARD)

Advertising the grand opening of our cannabis/hemp shop in NC. We will sell all things hemp (flower, cartridges, disposables, edibles, creams, lotions, pet products etc...)

Requirements
Must have
• include, open starting Aug 1, but grand opening Aug 15th.
Nice to have
• Difference slogan ideas "Save some cash, buy our grass" "Find your perfect high at Reed & Vale cannabis store" "Experience Nature's Gift: Reed & Vale Cannabis Store"

```html
<!DOCTYPE html>
<html lang="en">
<head>
<meta charset="utf-8">
<title>Reed &amp; Vale Billboard</title>
<link rel="stylesheet" href="https://fonts.googleapis.com/css2?family=Poppins:wght@400;500;700&display=swap">
<style>
  :root {
    --page-bg: #d4d4d4;
    --board-bg: #04050b;
    --leaf-green: #79c143;
    --leaf-deep: #2f5a16;
    --text-white: #ffffff;
  }
  * { margin: 0; padding: 0; box-sizing: border-box; }
  html, body {
    width: 958px;
    height: 1200px;
    overflow: hidden;
    background: var(--page-bg);
    font-family: "Poppins", sans-serif;
  }
  .billboard {
    position: absolute;
    left: 29px;
    top: 467px;
    width: 900px;
    height: 266px;
    background: var(--board-bg);
    overflow: hidden;
    box-shadow: 6px 10px 14px rgba(0, 0, 0, 0.35);
  }
  .leaf-photo {
    position: absolute;
    right: 0;
    top: 0;
    width: 520px;
    height: 100%;
    background:
      radial-gradient(ellipse 60% 70% at 80% 20%, rgba(121, 193, 67, 0.55), transparent 70%),
      radial-gradient(ellipse 40% 90% at 98% 70%, rgba(121, 193, 67, 0.6), transparent 70%),
      linear-gradient(100deg, transparent 0%, rgba(47, 90, 22, 0.35) 45%, rgba(47, 90, 22, 0.7) 100%);
  }
  .copy {
    position: absolute;
    left: 46px;
    top: 48px;
  }
  .headline {
    font-weight: 700;
    font-size: 61px;
    line-height: 0.98;
    letter-spacing: -0.5px;
  }
  .headline-top { color: var(--text-white); }
  .headline-bottom { color: var(--leaf-green); }
  .address {
    display: flex;
    align-items: center;
    gap: 6px;
    margin-top: 14px;
    color: var(--text-white);
    font-weight: 500;
    font-size: 29px;
  }
  .address svg { width: 20px; height: 26px; flex: none; }
  .opening-dates {
    position: absolute;
    right: 60px;
    top: 96px;
    text-align: right;
    color: var(--text-white);
    font-weight: 700;
    font-size: 17px;
    line-height: 1.3;
    letter-spacing: 0.3px;
  }
  .opening-dates .grand { color: var(--leaf-green); }
  .brand-name {
    position: absolute;
    right: 60px;
    bottom: 36px;
    color: var(--text-white);
    font-weight: 500;
    font-size: 36px;
    letter-spacing: -0.5px;
  }
</style>
</head>
<body>
  <section class="billboard">
    <div class="leaf-photo" role="img" aria-label="Close-up photo of green hemp leaves against a dark background"></div>
    <div class="copy">
      <h1 class="headline">
        <span class="headline-top">$AVE SOME CASH</span><br>
        <span class="headline-bottom">BUY OUR GRASS</span>
      </h1>
      <p class="address">
        <svg viewBox="0 0 20 26" aria-hidden="true">
          <path d="M10 1a8 8 0 0 0-8 8c0 6 8 15 8 15s8-9 8-15a8 8 0 0 0-8-8z" fill="none" stroke="var(--leaf-green)" stroke-width="3"/>
          <circle cx="10" cy="9" r="3" fill="var(--leaf-green)"/>
        </svg>
        482 Harlow Mill Rd
      </p>
    </div>
    <p class="opening-dates">
      OPEN STARTING AUG 1<br>
      <span class="grand">GRAND OPENING AUG 15TH</span>
    </p>
    <p class="brand-name">Reed &amp; Vale</p>
  </section>
</body>
</html>
```